Redesign of an insurance website

Attached is an insurance website that I need to redesign. Currently the website is too dark. I like for example www.brambleshield.com . Could you make the website lighter and change the structure a little so that it is more user friendly?

Industry/Entity Type

Insurance

Number of Pages Required

4 page

```html
<!DOCTYPE html>
<html lang="en">
<head>
<meta charset="utf-8">
<title>Contact Us – Kryleon.cz</title>
<link href="https://fonts.googleapis.com/css2?family=Lato:wght@400;700;900&family=Poppins:wght@400&display=swap" rel="stylesheet">
<style>
:root{
  --brand:#27b7ec;
  --brand-dark:#1fa6d8;
  --ink:#222222;
  --header-bg:#f0f9fd;
  --section-grey:#f5f5f5;
  --white:#ffffff;
  --footer-dark:#2b2e33;
  --muted:#c9cdd2;
}
*{box-sizing:border-box;margin:0;padding:0}
html,body{width:1200px;height:1066px;overflow:hidden}
body{font-family:'Lato',sans-serif;color:var(--ink);background:var(--white);position:relative}
.topbar{position:absolute;left:0;top:0;width:1200px;height:30px;background:var(--brand);color:var(--white)}
.social{position:absolute;left:119px;top:9px;display:flex;gap:14px}
.social span{width:12px;height:12px;border-radius:50%;background:var(--white);opacity:.9}
.account{position:absolute;right:120px;top:0;height:30px;display:flex;align-items:center;font-size:12px}
.account a{display:flex;align-items:center;gap:5px;color:var(--white);text-decoration:none}
.account .sep{width:1px;height:16px;background:rgba(255,255,255,.4);margin:0 13px}
.header{position:absolute;left:0;top:30px;width:1200px;height:56px;background:var(--header-bg)}
.logo{position:absolute;left:120px;top:14px;display:flex;align-items:center;gap:8px;font-weight:900;font-size:24px;letter-spacing:.5px;color:var(--ink)}
.logo i{width:14px;height:14px;border-radius:50%;background:var(--brand);display:block}
.search-btn{position:absolute;left:1051px;top:9px;width:28px;height:19px;background:var(--brand);border-radius:2px;display:flex;align-items:center;justify-content:center}
.nav{position:absolute;right:121px;top:34px;display:flex;gap:18px;font-size:13px}
.nav a{color:var(--ink);text-decoration:none;padding-bottom:4px}
.nav a.active{color:var(--brand);border-bottom:3px solid var(--brand)}
.hero{position:absolute;left:0;top:86px;width:1200px;height:155px;background:linear-gradient(100deg,#3a3430 0%,#5b5550 35%,#6e6a66 60%,#4e4a48 100%)}
.hero-text{position:absolute;left:0;top:86px;width:1200px;height:155px;text-align:center;color:var(--white)}
.hero-text h1{font-size:28px;font-weight:900;margin-top:52px}
.hero-text p{font-size:12px;font-weight:700;margin-top:1px}
.cards{position:absolute;left:121px;top:289px;display:flex;gap:18px}
.card{width:308px;height:93px;background:var(--brand);color:var(--white);display:flex;align-items:center}
.card.dark{background:var(--ink)}
.card .icon{width:86px;display:flex;justify-content:center}
.card h3{font-size:16px;font-weight:700;margin-bottom:5px}
.card p{font-size:13.5px;line-height:20px}
.contact{position:absolute;left:0;top:418px;width:1200px;height:407px;background:var(--section-grey)}
.contact h2{position:absolute;left:0;top:26px;width:1200px;text-align:center;font-size:31px;font-weight:900}
.contact h2 span{color:var(--brand)}
.field{position:absolute;background:var(--white);border:1px solid #ececec;border-radius:2px;font-family:'Poppins',sans-serif;font-size:12px;padding:13px 15px;color:var(--ink)}
.send{position:absolute;left:120px;top:334px;width:85px;height:36px;background:var(--ink);color:var(--white);font-size:15px;display:flex;align-items:center;justify-content:center;border-radius:2px}
.footer{position:absolute;left:0;top:825px;width:1200px;height:241px;background:linear-gradient(110deg,#26292d 0%,#3a3d42 45%,#2e3135 100%)}
.newsletter{position:absolute;left:165px;top:854px;width:861px;height:143px;background:var(--white);border-radius:12px}
.newsletter h3{position:absolute;left:49px;top:44px;font-size:25px;font-weight:900;color:var(--brand)}
.newsletter p{position:absolute;left:49px;top:76px;font-size:17px}
.sub-input{position:absolute;left:342px;top:55px;width:300px;height:38px;border:1px solid #d8d8d8;border-radius:19px 0 0 19px;font-size:11px;padding:12px 28px;color:#333}
.sub-btn{position:absolute;left:621px;top:54px;width:193px;height:39px;background:var(--brand);color:var(--white);border-radius:20px;font-size:16px;display:flex;align-items:center;justify-content:center}
.footer-rule{position:absolute;left:0;top:1025px;width:1200px;height:1px;background:rgba(255,255,255,.18)}
.copyright{position:absolute;left:0;top:1037px;width:1200px;text-align:center;color:var(--white);font-size:13px}
</style>
</head>
<body>
<div class="topbar">
  <div class="social"><span></span><span></span><span></span><span></span></div>
  <div class="account">
    <a href="#"><svg width="11" height="12" viewBox="0 0 11 12"><circle cx="5.5" cy="3.2" r="3" fill="#fff"/><path d="M0 12c0-4 2.5-5.5 5.5-5.5S11 8 11 12z" fill="#fff"/></svg>SIGN IN</a>
    <span class="sep"></span>
    <a href="#"><svg width="10" height="12" viewBox="0 0 10 12"><path d="M2.5 5V3.5a2.5 2.5 0 0 1 5 0V5" stroke="#fff" stroke-width="1.6" fill="none"/><rect x="0.5" y="5" width="9" height="7" rx="1" fill="#fff"/></svg>SIGN UP</a>
  </div>
</div>

<header class="header">
  <div class="logo"><i></i>KRYLEON.CZ</div>
  <div class="search-btn"><svg width="11" height="11" viewBox="0 0 11 11"><circle cx="4.5" cy="4.5" r="3.3" stroke="#fff" stroke-width="1.8" fill="none"/><path d="M7 7l3 3" stroke="#fff" stroke-width="2"/></svg></div>
  <nav class="nav"><a href="#">ABOUT US</a><a href="#">FAQ'S</a><a href="#" class="active">CONTACT US</a></nav>
</header>

<div class="hero" role="img" aria-label="Photo of hands working with documents and a laptop on a desk"></div>
<div class="hero-text"><h1>CONTACT US</h1><p>HOME/CONTACT US</p></div>

<section class="cards">
  <div class="card">
    <div class="icon"><svg width="26" height="26" viewBox="0 0 24 24"><path d="M6.6 10.8a15 15 0 0 0 6.6 6.6l2.2-2.2c.3-.3.7-.4 1-.2 1.1.4 2.3.6 3.6.6.6 0 1 .4 1 1V20c0 .6-.4 1-1 1A17 17 0 0 1 3 4c0-.6.4-1 1-1h3.5c.6 0 1 .4 1 1 0 1.3.2 2.5.6 3.6.1.3 0 .7-.2 1z" fill="#fff"/></svg></div>
    <div><h3>PHONE NUMBER</h3><p>+123 456 789 00<br>+123 456 789 00</p></div>
  </div>
  <div class="card dark">
    <div class="icon"><svg width="28" height="22" viewBox="0 0 28 22"><rect x="1.5" y="1.5" width="25" height="19" rx="2" stroke="#fff" stroke-width="2.2" fill="none"/><path d="M2 3l12 9 12-9" stroke="#fff" stroke-width="2.2" fill="none"/></svg></div>
    <div><h3>EMAIL</h3><p>info@kryleon.cz</p></div>
  </div>
  <div class="card">
    <div class="icon"><svg width="44" height="42" viewBox="0 0 44 42"><rect x="20" y="3" width="4" height="36" fill="#fff"/><path d="M22 7h18l3 3-3 3H22z" fill="#fff"/><path d="M20 15H5l-4 3 4 3h15z" fill="#fff"/><rect x="15" y="38" width="14" height="3" fill="#fff"/></svg></div>
    <div><h3>LOCATION</h3><p>Praesent posuere, orci sit<br>rhoncus tincidunt, erat justo</p></div>
  </div>
</section>

<section class="contact">
  <h2>GET IN <span>TOUCH WITH US</span></h2>
  <div class="field" style="left:120px;top:89px;width:468px;height:39px">Name</div>
  <div class="field" style="left:610px;top:89px;width:469px;height:39px">Email</div>
  <div class="field" style="left:120px;top:145px;width:468px;height:39px">Subject</div>
  <div class="field" style="left:610px;top:145px;width:469px;height:39px">Phone</div>
  <div class="field" style="left:120px;top:200px;width:959px;height:116px">Message</div>
  <div class="send">SEND</div>
</section>

<footer class="footer" role="img" aria-label="Dimmed photo of people working at a desk with papers"></footer>
<div class="newsletter">
  <h3>SIGNUP NEWSLETTER</h3>
  <p>Get In Touch With Us</p>
  <div class="sub-input">Enter Email Address</div>
  <div class="sub-btn">SUBSCRIBE NOW</div>
</div>
<div class="footer-rule"></div>
<p class="copyright">Copyright © 2017 Kryleon. All right reserved.</p>
</body>
</html>
```